Tolvir Laundry and Dry Cleaning Poster

We need a Poster and Window Sticker for our Laundry and Dry cleaning shop (TOLVIR LAUNDRY AND DRY CLEANING).
info we like on the design. Logo is included
Company Name: Tolvir Laundry and Dry Cleaning
Slogan: It Comes Back Clean
Location: Kwelmo-Danfi, Accra
Working Hours: Mon-Sat 8am to 5pm
Tel: +233 30 418 7262
email:info@tolvirwash.example
website: www.tolvirwash.example
fb: fb.com/tolvirwash

Target Market(s)

Laundry Shop

Colors
33a6d7
9bcb3b

```html
<!DOCTYPE html>
<html lang="en">
<head>
<meta charset="utf-8">
<title>Tolvir Laundry and Dry Cleaning Poster</title>
<link rel="stylesheet" href="https://fonts.googleapis.com/css2?family=Bebas+Neue&display=swap">
<style>
  :root {
    --mat: #a1a2a6;
    --paper: #ffffff;
    --grid: #e4edf5;
    --brand-blue: #2ea3d8;
    --brand-teal: #17b3a0;
    --ink: #2a2a2a;
    --wave: #d6e6f6;
  }
  html, body {
    margin: 0;
    padding: 0;
    width: 1200px;
    height: 1200px;
    overflow: hidden;
    background: var(--mat);
  }
  .poster-canvas {
    display: block;
    width: 1200px;
    height: 1200px;
  }
  .type {
    font-family: "Bebas Neue", "Oswald", sans-serif;
  }
  .fill-blue { fill: var(--brand-blue); }
  .fill-teal { fill: var(--brand-teal); }
  .fill-ink { fill: var(--ink); }
  .fill-paper { fill: var(--paper); }
  .stroke-blue { stroke: var(--brand-blue); fill: none; }
  .stroke-teal { stroke: var(--brand-teal); fill: none; }
  .grid-line { stroke: var(--grid); stroke-width: 1; }
</style>
</head>
<body>
<svg class="poster-canvas" viewBox="0 0 1200 1200" xmlns="http://www.w3.org/2000/svg">
  <defs>
    <pattern id="paper-grid" width="16" height="16" patternUnits="userSpaceOnUse">
      <path class="grid-line" d="M16 0H0V16" fill="none"/>
    </pattern>
    <linearGradient id="photo-tone" x1="0" y1="0" x2="1" y2="1">
      <stop offset="0" stop-color="#f4f4f3"/>
      <stop offset="0.55" stop-color="#dcdcdc"/>
      <stop offset="1" stop-color="#8a8c90"/>
    </linearGradient>
    <linearGradient id="wave-tone" x1="0" y1="0" x2="1" y2="0">
      <stop offset="0" stop-color="#dbe8f6" stop-opacity="0.7"/>
      <stop offset="1" stop-color="#c9dcf1" stop-opacity="0.5"/>
    </linearGradient>
    <clipPath id="photo-clip">
      <path d="M0 0H484C480 150 380 290 230 303C130 310 50 285 0 240Z"/>
    </clipPath>
  </defs>

  <g class="poster" transform="translate(88 160)">
    <!-- paper -->
    <rect class="fill-paper" width="1032" height="878"/>
    <rect width="1032" height="878" fill="url(#paper-grid)" opacity="0.8"/>

    <!-- soft background wave -->
    <path d="M0 830C160 760 300 740 430 700C560 660 660 560 760 540C860 520 940 610 1032 560V878H0Z" fill="url(#wave-tone)" opacity="0.55"/>
    <path d="M260 878C420 800 560 760 680 690C780 630 880 600 1032 640" stroke="#c4d8ef" stroke-width="2" fill="none" opacity="0.6"/>

    <!-- photo area -->
    <g class="hero-photo" clip-path="url(#photo-clip)">
      <rect role="img" aria-label="Photo of a hand turning the dial of a white front-loading washing machine" width="484" height="310" fill="url(#photo-tone)"/>
    </g>
    <path class="stroke-teal" d="M484 80C476 200 390 300 230 306C130 309 50 283 0 240" stroke-width="8"/>
    <path class="fill-teal" d="M0 55C90 60 170 40 245 0H232C160 32 80 48 0 44Z"/>

    <!-- brand name -->
    <g class="brand-name">
      <circle class="fill-teal" cx="575" cy="176" r="22"/>
      <text class="type fill-blue" x="612" y="220" font-size="124" textLength="372" lengthAdjust="spacingAndGlyphs">TOLVIR</text>
      <text class="type fill-blue" x="612" y="256" font-size="28" textLength="372" lengthAdjust="spacingAndGlyphs">LAUNDRY AND DRY CLEANING</text>
    </g>

    <!-- headline -->
    <text class="type fill-blue" x="44" y="465" font-size="188" textLength="940" lengthAdjust="spacingAndGlyphs">TOLVIR LAUNDRY</text>
    <text class="type fill-blue" x="542" y="527" font-size="77" textLength="420" lengthAdjust="spacingAndGlyphs">AND DRY CLEANING</text>
    <text class="type fill-teal" x="294" y="601" font-size="71" textLength="446" lengthAdjust="spacingAndGlyphs">IT COMES BACK CLEAN</text>

    <!-- clock icon -->
    <g class="hours-icon">
      <circle class="stroke-blue" cx="516" cy="648" r="32" stroke-width="7"/>
      <circle class="stroke-blue" cx="516" cy="648" r="22" stroke-width="2"/>
      <path class="stroke-blue" d="M516 633V648L528 654" stroke-width="4" stroke-linecap="round"/>
    </g>

    <!-- working hours -->
    <text class="type fill-ink" x="412" y="723" font-size="40" textLength="212" lengthAdjust="spacingAndGlyphs">WORKING HOURS:</text>
    <rect class="fill-blue" x="368" y="734" width="122" height="50"/>
    <text class="type fill-paper" x="380" y="774" font-size="42" textLength="98" lengthAdjust="spacingAndGlyphs">MON-SAT</text>
    <text class="type fill-ink" x="493" y="772" font-size="38">:</text>
    <rect class="stroke-blue" x="503" y="735" width="164" height="48" stroke-width="2"/>
    <text class="type fill-ink" x="514" y="774" font-size="42" textLength="142" lengthAdjust="spacingAndGlyphs">8AM TO 5PM</text>

    <!-- location -->
    <g class="icon-pin">
      <ellipse class="stroke-blue" cx="61" cy="742" rx="15" ry="5" stroke-width="2"/>
      <path class="fill-blue" d="M61 742C52 730 50 724 50 718A11 11 0 0 1 72 718C72 724 70 730 61 742Z"/>
      <circle class="fill-paper" cx="61" cy="718" r="4"/>
    </g>
    <text class="type fill-ink" x="44" y="788" font-size="43" textLength="272" lengthAdjust="spacingAndGlyphs">KWELMO-DANFI, ACCRA</text>

    <!-- phone -->
    <g class="icon-phone">
      <ellipse class="stroke-blue" cx="760" cy="742" rx="15" ry="5" stroke-width="2"/>
      <path class="fill-blue" d="M760 742C751 730 749 724 749 718A11 11 0 0 1 771 718C771 724 769 730 760 742Z"/>
      <circle class="fill-paper" cx="760" cy="718" r="6"/>
      <path d="M757 715Q757 721 763 722" stroke="var(--ink)" stroke-width="2" fill="none"/>
    </g>
    <text class="type fill-ink" x="748" y="788" font-size="43" textLength="240" lengthAdjust="spacingAndGlyphs">+233 30 418 7262</text>

    <!-- web -->
    <g class="icon-web">
      <path class="fill-blue" d="M54 834C46 824 43 818 43 812A11 11 0 0 1 65 812C65 818 62 824 54 834Z"/>
      <circle class="fill-ink" cx="54" cy="812" r="6"/>
      <path d="M48 812H60M54 806V818" stroke="#fff" stroke-width="1"/>
    </g>
    <text class="type fill-ink" x="72" y="836" font-size="32" textLength="228" lengthAdjust="spacingAndGlyphs">WWW.TOLVIRWASH.EXAMPLE</text>

    <!-- social page -->
    <g class="icon-social">
      <path class="fill-blue" d="M404 834C396 824 393 818 393 812A11 11 0 0 1 415 812C415 818 412 824 404 834Z"/>
      <circle class="fill-paper" cx="404" cy="812" r="5"/>
    </g>
    <text class="type fill-ink" x="422" y="836" font-size="32" textLength="208" lengthAdjust="spacingAndGlyphs">FB.COM/TOLVIRWASH</text>

    <!-- email -->
    <g class="icon-mail">
      <path class="fill-blue" d="M734 834C726 824 723 818 723 812A11 11 0 0 1 745 812C745 818 742 824 734 834Z"/>
      <rect class="fill-ink" x="728" y="808" width="12" height="8"/>
      <path d="M728 808L734 813L740 808" stroke="#fff" stroke-width="1" fill="none"/>
    </g>
    <text class="type fill-ink" x="754" y="836" font-size="32" textLength="234" lengthAdjust="spacingAndGlyphs">INFO@TOLVIRWASH.EXAMPLE</text>
  </g>
</svg>
</body>
</html>
```